Website for boutique digital agency helping high-tech startups accelerate growth.

We need a website design for a relatively young company based in Mauritius called 'LumaTrel'.

We are a professional services firm delivering digital infrastructure for revenue operations (RevOps)*.

Entrepreneurial startups and SMBs in the technology sector work with us to accelerate growth by delivering extraordinary customer experiences across the full customer lifecycle.

We would like a colourful design that utilises the (4) colours of our existing logo design.

The final design should communicate dynamic growth through relentless customer focus.
----------------------------------------------------------
*Revenue Operations (RevOps) is the strategic alignment of sales, marketing and customer success operations to accelerate growth by delivering extraordinary customer experiences across the full customer life cycle.

Target Market(s)

Entrepreneurial startups and SMBs (Small/Medium Businesses) in the technology sector.

Question: Why the technology sector?

Answer: Because technology entrepreneurs often have a tremendous challenge to effectively communicate to the market and to prospective customers the value and the benefits of their products & services due to the inherent complexity of technological innovation.

LumaTrel is a team of creatively-minded engineers and technologists who have worked with and understand the technologies and innovations our clients are passionate about bringing to market.

Industry/Entity Type

Professional Service

Number of Pages Required

5+ page

Font styles to use
Sans Serif

Requirements
Must have
• Minimalistic designs rich with visual meaning are highly preferred. Mobile responsive designs are also required. Must show how designs render on Desktop, Tablet and Smartphone devices.

Website pages:
1) Homepage: problem statement, target customers, value proposition & benefits
2) Services: 3-4 tiers of services packages with pricing and "how to work with us"
3) Resources: links to all kinds of relevant materials
4) Contact Us: contact form and special project quote form
5) Blog: matrix design with featured images for each post
Nice to have
• Bold, interesting, colourful, inspiring images that visually communicate:
- relentless customer focus
- extraordinary, memorable experiences
- business at the speed of innovation
Should not have
• Any meme or theme that panders to "political correctness".

```html
<!DOCTYPE html>
<html lang="en">
<head>
<meta charset="utf-8">
<title>LumaTrel — Revenue Operations</title>
<link href="https://fonts.googleapis.com/css2?family=Montserrat:wght@500;600;700;800&family=Raleway:wght@400;500;600&display=swap" rel="stylesheet">
<style>
:root{
  --orange:#fb5c0b;
  --green:#7dc421;
  --red:#e5112e;
  --teal:#1b7d79;
  --teal-deep:#0e4a49;
  --ink:#222;
  --muted:#555;
  --panel:#e9e9e9;
  --row:#ececec;
  --white:#fff;
}
*{box-sizing:border-box;margin:0;padding:0}
html,body{width:1200px;height:3717px;overflow:hidden}
body{position:relative;background:#fff;font-family:"Raleway",sans-serif;color:var(--ink)}
.abs{position:absolute}
h1,h2,h3,h4,.head{font-family:"Montserrat",sans-serif}

/* header */
.brand{left:79px;top:36px;display:flex;align-items:center;gap:10px;font-family:"Montserrat",sans-serif;font-weight:700;font-size:30px;color:#3a3a3a}
.brand-mark{width:14px;height:14px;background:var(--orange)}
.nav{left:601px;top:32px;display:flex;align-items:center;font-family:"Montserrat",sans-serif;font-size:13px;font-weight:500}
.nav a{color:#222;text-decoration:none;text-transform:uppercase}
.nav .active{background:var(--green);color:#fff;width:81px;height:37px;display:flex;align-items:center;justify-content:center;font-weight:600;margin-right:68px}
.nav .r{margin-right:50px}
.nav .s{margin-right:48px}
.nav .c{margin-right:48px}

.social{left:25px;width:28px;height:28px;border-radius:50%}
.pager{left:1154px;width:13px;height:13px;border:2px solid #222}
.pager.on{border-color:var(--orange)}

/* hero */
.city-band{left:0;top:499px;width:1200px;height:568px;background:linear-gradient(180deg,#1c6d6a 0%,#124f4e 45%,#0b3433 100%)}
.city-strip{left:0;top:1067px;width:199px;height:450px;background:linear-gradient(180deg,#0b3433,#0f2d2c)}
.hero{left:79px;top:100px;width:1040px;height:499px;border-radius:4px;background:linear-gradient(180deg,#a9b8ba 0%,#7d918b 35%,#4f6a55 65%,#2e4a3a 100%)}
.hero-lead{left:79px;top:192px;width:1040px;text-align:center;color:#fff;font-size:22px;line-height:30px;font-weight:400}
.hero-tag{left:79px;top:481px;width:1040px;text-align:center;color:#fff;font-size:22px}
.hero-tag b{font-family:"Montserrat",sans-serif;font-weight:700}

/* what is revops */
.what-title{left:82px;top:740px;color:#fff;font-size:33px;font-weight:700}
.what-rule{left:82px;top:793px;width:29px;height:3px;background:#fff}
.what-copy{left:80px;top:816px;width:410px;color:#fff;font-size:12.5px;line-height:17px}
.what-copy p+p{margin-top:16px}
.pillar{width:250px;height:99px;background:#fff;border-radius:3px;display:flex;align-items:center;padding-left:28px;gap:18px}
.pillar .num{width:51px;height:51px;border-radius:50%;display:flex;align-items:center;justify-content:center;color:#fff;font-family:"Montserrat",sans-serif;font-weight:800;font-size:24px;flex:none}
.pillar h3{font-size:16px;font-weight:600;color:#111;margin-bottom:4px}
.pillar p{font-size:12.5px;line-height:16px;color:#222}

/* resources */
.res-panel{left:199px;top:1067px;width:1001px;height:599px;background:var(--panel)}
.sec-title{width:100%;text-align:center;font-family:"Montserrat",sans-serif;font-weight:700;font-size:33px;color:#111}
.sec-sub{width:100%;text-align:center;font-size:11px;line-height:14px;color:#222}
.tile{overflow:hidden;border-radius:2px}
.tile .photo{position:absolute;inset:0}
.tile h4{position:absolute;left:20px;top:18px;right:16px;color:#fff;font-size:14px;line-height:19px;font-weight:700}
.tile .rule{position:absolute;left:20px;width:29px;height:2px;background:#fff}
.tile .more{position:absolute;left:20px;height:28px;padding:0 11px;background:#fff;border-radius:2px;font-family:"Montserrat",sans-serif;font-size:10.5px;font-weight:700;display:flex;align-items:center}

/* pricing */
.plan{width:238px;height:578px;border:1px solid;background:#fff}
.plan header{height:48px;display:flex;align-items:center;justify-content:center;color:#fff;font-family:"Montserrat",sans-serif;font-weight:700;font-size:14px;text-transform:uppercase}
.plan .price{height:103px;display:flex;align-items:center;justify-content:center;font-family:"Montserrat",sans-serif;font-weight:800;font-size:45px;color:#111}
.plan ul{list-style:none}
.plan li{height:30px;display:flex;align-items:center;font-size:12.5px;color:#333;padding-left:60px;position:relative}
.plan li:nth-child(odd){background:var(--row)}
.plan li svg{position:absolute;left:22px;top:8px}
.plan .buy{margin:32px auto 0;width:130px;height:39px;display:flex;align-items:center;justify-content:center;color:#fff;font-family:"Montserrat",sans-serif;font-weight:700;font-size:14px;border-radius:2px}

/* contact */
.green-bg{left:1000px;top:2993px;width:200px;height:151px;background:linear-gradient(180deg,#5f9e1e,#3f7a18)}
.contact-panel{left:0;top:2546px;width:1000px;height:598px;background:var(--panel)}
.form-box{left:100px;top:2729px;width:500px;height:350px;background:#fff}
.field{border:1.5px solid #f6a47c;border-radius:2px;height:39px;font-size:11.5px;color:#aaa;padding:0 13px;display:flex;align-items:center}
.field.area{align-items:flex-start;padding-top:10px}
.send{left:141px;top:3023px;width:419px;height:29px;background:var(--orange);color:#fff;display:flex;align-items:center;justify-content:center;font-size:13px;font-weight:600;border-radius:2px}
.info{left:600px;top:2729px;width:300px;height:350px;background:var(--orange);color:#fff}
.info h3{position:absolute;left:38px;top:38px;font-size:16px;font-weight:600}
.info .line{position:absolute;left:82px;font-size:12.5px;line-height:17px}
.info svg{position:absolute;left:38px}

/* newsletter */
.news{left:0;top:3144px;width:1200px;height:303px;background:linear-gradient(180deg,#5a9a1c 0%,#3f7d19 55%,#2c5e17 100%)}
.news-title{left:141px;top:3250px;color:#fff;font-family:"Montserrat",sans-serif;font-weight:800;font-size:33px;line-height:43px;text-transform:uppercase}
.news-input{left:661px;top:3276px;width:200px;height:39px;background:#fff;border-radius:2px;font-size:12px;color:#aaa;display:flex;align-items:center;padding-left:18px}
.news-btn{left:871px;top:3276px;width:131px;height:39px;background:var(--red);color:#fff;border-radius:2px;font-size:12.5px;font-weight:600;display:flex;align-items:center;justify-content:center}

/* footer */
.footer{left:0;top:3447px;width:1200px;height:270px;background:var(--teal)}
.fcol{top:3527px;color:#fff}
.fcol h4{font-size:16px;font-weight:600;margin-bottom:20px}
.fcol a{display:block;color:#fff;text-decoration:none;font-size:13px;line-height:24px}
</style>
</head>
<body>

<!-- header -->
<div class="abs brand"><span class="brand-mark"></span>LumaTrel</div>
<nav class="abs nav">
  <a class="active" href="#">Home</a>
  <a class="r" href="#">Resources</a>
  <a class="s" href="#">Services</a>
  <a class="c" href="#">Contact Us</a>
  <a href="#">Blog</a>
</nav>

<!-- background bands -->
<div class="abs city-band" role="img" aria-label="Dark teal-tinted aerial city skyline"></div>
<div class="abs city-strip" role="img" aria-label="City skyline at dusk continuing behind the resources panel"></div>

<!-- social -->
<span class="abs social" style="top:263px;background:#1da1f2"></span>
<span class="abs social" style="top:311px;background:#2a6fb8"></span>
<span class="abs social" style="top:358px;background:#3b5bb5"></span>
<span class="abs social" style="top:406px;background:#d23b7a"></span>

<span class="abs pager on" style="top:321px"></span>
<span class="abs pager" style="top:343px"></span>
<span class="abs pager" style="top:366px"></span>

<!-- hero -->
<div class="abs hero" role="img" aria-label="Futuristic green city skyline with wind turbines, trains and flying vehicles"></div>
<p class="abs hero-lead">We believe the world has changed – Marketing, Sales, and Customer Success<br>need to operate across the full funnel to drive growth.</p>
<p class="abs hero-tag">We call this <b>Revenue Operations.</b></p>

<!-- what is revops -->
<h2 class="abs what-title">What is RevOps?</h2>
<span class="abs what-rule"></span>
<div class="abs what-copy">
  <p>Revenue Operations, or RevOps, is a new department that manag-<br>es full funnel operations across Marketing,<br>Sales, and Customer Success.</p>
  <p>RevOps brings together four areas of responsibility from depart-<br>mental silos: Operations, Enablement,<br>Insights, and Tools.</p>
</div>

<div class="abs pillar" style="left:591px;top:718px"><span class="num" style="background:var(--orange)">1</span><div><h3>Operations</h3><p>Lorem ipsum dolor<br>sit amet.</p></div></div>
<div class="abs pillar" style="left:870px;top:718px"><span class="num" style="background:var(--green)">2</span><div><h3>Enablement</h3><p>Lorem ipsum dolor<br>sit amet.</p></div></div>
<div class="abs pillar" style="left:591px;top:847px"><span class="num" style="background:var(--teal)">3</span><div><h3>Insights</h3><p>Lorem ipsum dolor<br>sit amet.</p></div></div>
<div class="abs pillar" style="left:870px;top:847px"><span class="num" style="background:var(--red)">4</span><div><h3>Tools</h3><p>Lorem ipsum dolor<br>sit amet.</p></div></div>

<!-- resources -->
<section class="abs res-panel"></section>
<h2 class="abs sec-title" style="left:199px;width:1001px;top:1112px">RESOURCES</h2>
<p class="abs sec-sub" style="left:199px;width:1001px;top:1157px">In-depth explanation about Revenue Operations</p>

<article class="abs tile" style="left:317px;top:1197px;width:375px;height:147px">
  <div class="photo" role="img" aria-label="Green-tinted circuit board close-up" style="background:linear-gradient(135deg,#2f7d14,#5fae22 60%,#3d8a18)"></div>
  <h4>How technology changes<br>our life?</h4><span class="rule" style="top:65px"></span>
  <span class="more" style="top:99px;color:var(--green)">Read more</span>
</article>
<article class="abs tile" style="left:708px;top:1197px;width:179px;height:248px">
  <div class="photo" role="img" aria-label="Orange-tinted tablet showing business charts" style="background:linear-gradient(160deg,#e4560c,#b7400a 60%,#8a2f08)"></div>
  <h4>Is Revenue Analyst<br>a good carreer?</h4><span class="rule" style="top:72px"></span>
  <span class="more" style="top:198px;color:var(--orange)">Read more</span>
</article>
<article class="abs tile" style="left:903px;top:1197px;width:180px;height:248px">
  <div class="photo" role="img" aria-label="Green-tinted team hands joined over a desk" style="background:linear-gradient(160deg,#2b6a12,#5aa222 55%,#3c7d18)"></div>
  <h4>How RevOps lead<br>your business to<br>growth bigger</h4><span class="rule" style="top:88px"></span>
  <span class="more" style="top:198px;color:var(--green)">Read more</span>
</article>
<article class="abs tile" style="left:317px;top:1360px;width:181px;height:250px">
  <div class="photo" role="img" aria-label="Orange-tinted workspace with desk and bridge view" style="background:linear-gradient(160deg,#e65a0c,#c4460a 60%,#9a360a)"></div>
  <h4>Revenue Ops is<br>here: Expectation<br>for 2019<br>and beyond</h4><span class="rule" style="top:110px"></span>
  <span class="more" style="top:200px;color:var(--orange)">Read more</span>
</article>
<article class="abs tile" style="left:513px;top:1360px;width:179px;height:250px">
  <div class="photo" role="img" aria-label="Teal-tinted office documents and charts" style="background:linear-gradient(160deg,#1a7773,#238a84 55%,#14615e)"></div>
  <h4>What is the<br>differences<br>between sales and<br>operations?</h4><span class="rule" style="top:110px"></span>
  <span class="more" style="top:200px;color:var(--teal)">Read more</span>
</article>
<article class="abs tile" style="left:708px;top:1461px;width:375px;height:149px">
  <div class="photo" role="img" aria-label="Red-tinted audience at a conference" style="background:linear-gradient(135deg,#c30f26,#e5112e 55%,#a10c20)"></div>
  <h4>Professional guide to Revenue Operation by<br>Dana Verholt</h4><span class="rule" style="top:65px"></span>
  <span class="more" style="top:99px;color:var(--red)">Read more</span>
</article>

<!-- features / pricing -->
<h2 class="abs sec-title" style="left:0;top:1752px">FEATURES</h2>
<p class="abs sec-sub" style="left:0;top:1801px">Nulla at pulvinar risus. Nulla sit amet accumsan ex, at aliquet magna.<br>Etiam vitae tincidunt nulla, a euismod velit. Donec congue varius egestas.</p>

<svg width="0" height="0" style="position:absolute">
  <defs><symbol id="tick" viewBox="0 0 16 14"><path d="M1 7.5l4.5 4.5L15 1.5" fill="none" stroke="currentColor" stroke-width="3" stroke-linecap="round" stroke-linejoin="round"/></symbol></defs>
</svg>

<div class="abs plan" style="left:105px;top:1861px;border-color:var(--orange);--c:var(--orange)">
  <header style="background:var(--orange)">Basic</header>
  <div class="price">$29</div>
  <ul style="color:var(--orange)">
    <li><svg width="16" height="14"><use href="#tick"/></svg>Mauris sit amet dui eu</li>
    <li><svg width="16" height="14"><use href="#tick"/></svg>Erat aliquet ullamcorper</li>
    <li><svg width="16" height="14"><use href="#tick"/></svg>Vestibulum mattis odio id</li>
    <li><svg width="16" height="14"><use href="#tick"/></svg>Mauris hendrerit blandit</li>
    <li>Morbi accumsan ipsum</li>
    <li>Eu maximus euismod</li>
    <li>Sed finibus sem ut</li>
    <li>Nunc eleifend lectus nec</li>
    <li>Aliquam auctor eros</li>
    <li>Eu arcu vehicula</li>
    <li>Sodales sapien sollicitudin</li>
  </ul>
  <a class="buy" style="background:var(--orange)">BUY NOW</a>
</div>

<div class="abs plan" style="left:356px;top:1861px;border-color:var(--green)">
  <header style="background:var(--green)">Standard</header>
  <div class="price">$39</div>
  <ul style="color:var(--green)">
    <li><svg width="16" height="14"><use href="#tick"/></svg>Mauris sit amet dui eu</li>
    <li><svg width="16" height="14"><use href="#tick"/></svg>Erat aliquet ullamcorper</li>
    <li><svg width="16" height="14"><use href="#tick"/></svg>Vestibulum mattis odio id</li>
    <li><svg width="16" height="14"><use href="#tick"/></svg>Mauris hendrerit blandit</li>
    <li><svg width="16" height="14"><use href="#tick"/></svg>Morbi accumsan ipsum</li>
    <li><svg width="16" height="14"><use href="#tick"/></svg>Eu maximus euismod</li>
    <li>Sed finibus sem ut</li>
    <li>Nunc eleifend lectus nec</li>
    <li>Aliquam auctor eros</li>
    <li>Eu arcu vehicula</li>
    <li>Sodales sapien sollicitudin</li>
  </ul>
  <a class="buy" style="background:var(--green)">BUY NOW</a>
</div>

<div class="abs plan" style="left:606px;top:1861px;border-color:var(--red)">
  <header style="background:var(--red)">Business</header>
  <div class="price">$49</div>
  <ul style="color:var(--red)">
    <li><svg width="16" height="14"><use href="#tick"/></svg>Mauris sit amet dui eu</li>
    <li><svg width="16" height="14"><use href="#tick"/></svg>Erat aliquet ullamcorper</li>
    <li><svg width="16" height="14"><use href="#tick"/></svg>Vestibulum mattis odio id</li>
    <li><svg width="16" height="14"><use href="#tick"/></svg>Mauris hendrerit blandit</li>
    <li><svg width="16" height="14"><use href="#tick"/></svg>Morbi accumsan ipsum</li>
    <li><svg width="16" height="14"><use href="#tick"/></svg>Eu maximus euismod</li>
    <li><svg width="16" height="14"><use href="#tick"/></svg>Sed finibus sem ut</li>
    <li><svg width="16" height="14"><use href="#tick"/></svg>Nunc eleifend lectus nec</li>
    <li>Aliquam auctor eros</li>
    <li>Eu arcu vehicula</li>
    <li>Sodales sapien sollicitudin</li>
  </ul>
  <a class="buy" style="background:var(--red)">BUY NOW</a>
</div>

<div class="abs plan" style="left:855px;top:1861px;border-color:var(--teal)">
  <header style="background:var(--teal)">Professional</header>
  <div class="price">$199</div>
  <ul style="color:var(--teal)">
    <li><svg width="16" height="14"><use href="#tick"/></svg>Mauris sit amet dui eu</li>
    <li><svg width="16" height="14"><use href="#tick"/></svg>Erat aliquet ullamcorper</li>
    <li><svg width="16" height="14"><use href="#tick"/></svg>Vestibulum mattis odio id</li>
    <li><svg width="16" height="14"><use href="#tick"/></svg>Mauris hendrerit blandit</li>
    <li><svg width="16" height="14"><use href="#tick"/></svg>Morbi accumsan ipsum</li>
    <li><svg width="16" height="14"><use href="#tick"/></svg>Eu maximus euismod</li>
    <li><svg width="16" height="14"><use href="#tick"/></svg>Sed finibus sem ut</li>
    <li><svg width="16" height="14"><use href="#tick"/></svg>Nunc eleifend lectus nec</li>
    <li><svg width="16" height="14"><use href="#tick"/></svg>Aliquam auctor eros</li>
    <li><svg width="16" height="14"><use href="#tick"/></svg>Eu arcu vehicula</li>
    <li><svg width="16" height="14"><use href="#tick"/></svg>Sodales sapien sollicitudin</li>
  </ul>
  <a class="buy" style="background:var(--teal)">BUY NOW</a>
</div>

<!-- contact -->
<div class="abs green-bg" role="img" aria-label="Green forested hillside"></div>
<section class="abs contact-panel"></section>
<h2 class="abs sec-title" style="left:0;width:1000px;top:2610px">CONTACT US</h2>
<p class="abs sec-sub" style="left:0;width:1000px;top:2656px">Nulla at pulvinar risus. Nulla sit amet accumsan ex, at aliquet magna.<br>Etiam vitae tincidunt nulla, a euismod velit. Donec congue varius egestas.</p>

<div class="abs form-box"></div>
<div class="abs field" style="left:141px;top:2769px;width:199px">Name</div>
<div class="abs field" style="left:361px;top:2769px;width:199px">Phone Number</div>
<div class="abs field" style="left:141px;top:2830px;width:199px">Email</div>
<div class="abs field" style="left:361px;top:2830px;width:199px">Subject</div>
<div class="abs field area" style="left:141px;top:2890px;width:419px;height:111px">Type your message in here...</div>
<div class="abs send">Send Message</div>

<div class="abs info">
  <h3>Contact Information</h3>
  <svg style="top:117px" width="16" height="20" viewBox="0 0 16 20"><path d="M8 1a6 6 0 0 0-6 6c0 4.5 6 12 6 12s6-7.5 6-12a6 6 0 0 0-6-6z" fill="none" stroke="#fff" stroke-width="2"/><circle cx="8" cy="7" r="2.2" fill="#fff"/></svg>
  <p class="line" style="top:120px">18 Corvell Lane<br>Port Amsel<br>Riverton, 40112</p>
  <svg style="top:186px" width="20" height="20" viewBox="0 0 20 20"><path d="M4 1l4 4-2.5 2.5a11 11 0 0 0 7 7L15 12l4 4-3 3C8 19 1 12 1 4z" fill="#fff"/></svg>
  <p class="line" style="top:188px">+230 555 0147</p>
  <svg style="top:236px" width="20" height="14" viewBox="0 0 20 14"><rect width="20" height="14" rx="1.5" fill="#fff"/><path d="M1 1.5l9 6.5 9-6.5" fill="none" stroke="var(--orange)" stroke-width="1.8"/></svg>
  <p class="line" style="top:234px">hello@lumatrel.example</p>
  <svg style="top:284px" width="20" height="20" viewBox="0 0 20 20"><circle cx="10" cy="10" r="9" fill="#fff"/><path d="M10 1c-3 3-3 15 0 18M10 1c3 3 3 15 0 18M1 10h18M3 5h14M3 15h14" fill="none" stroke="var(--orange)" stroke-width="1.3"/></svg>
  <p class="line" style="top:286px">www.lumatrel.example</p>
</div>

<!-- newsletter -->
<section class="abs news" role="img" aria-label="Green-tinted aerial view of a forested city"></section>
<h2 class="abs news-title">Subscribe<br>our newsletter</h2>
<div class="abs news-input">Enter email</div>
<div class="abs news-btn">Subscribe Now</div>

<!-- footer -->
<footer class="abs footer"></footer>
<div class="abs fcol" style="left:141px"><h4>Community</h4><a>Donec</a><a>Malesuada</a><a>Lacus</a><a>Porttitor</a><a>Risus</a></div>
<div class="abs fcol" style="left:346px"><h4>Abous Us</h4><a>Donec</a><a>Malesuada</a><a>Lacus</a><a>Porttitor</a><a>Risus</a></div>
<div class="abs fcol" style="left:538px"><h4>Costumer Care</h4><a>Donec</a><a>Malesuada</a><a>Lacus</a><a>Porttitor</a><a>Risus</a></div>
<div class="abs fcol" style="left:764px"><h4>Contact Us</h4><a>Donec</a><a>Malesuada</a><a>Lacus</a><a>Porttitor</a><a>Risus</a></div>
<div class="abs fcol" style="left:950px"><h4>How It Works</h4><a>Donec</a><a>Malesuada</a><a>Lacus</a><a>Porttitor</a><a>Risus</a></div>

</body>
</html>
```